Flyer für Tiertherapeutin
Eine sehr motivierte und kreative Designerin. Schon der erste Vorschlag war ganz nach meinen Vorstellungen.
Zielgruppe
Ich bin Tiertherapeutin für TCVM und Ernährungsberaterin für Hunde und Katzen. Mittels Akupunktur, Lasertherapie, Mykotherapie und Ernährungsberatung kommt es zu einer Linderung vorhandener Schmerzen, eine verbesserte Regulation der Organe und einer Steigerung das Wohlbefindens sowie Lebensqualität.
Zielgruppe sind überwiegend weibliche Hunde- und Katzenbesitzer mit erkrankten Tieren.
Aufgabenstellung
Flyer sollte klappbar sein. Logo und mein Name und Kontaktdaten sollten enthalten sein.

```html
<!DOCTYPE html>
<html lang="de">
<head>
<meta charset="utf-8">
<title>Pfotenruhe – Flyer</title>
<link rel="stylesheet" href="https://fonts.googleapis.com/css2?family=Fredoka:wght@600;700&family=Poppins:wght@400;600&family=Playfair+Display:wght@700&family=Kaushan+Script&display=swap">
<style>
:root{
  --bg:#dde0e3;
  --paper:#f7f7f6;
  --tan:#c9935f;
  --tan-light:#d9a877;
  --olive:#4e4a26;
  --ink:#2a2416;
  --text:#2e2e2e;
  --white:#ffffff;
  --rule:#dcdcdc;
}
*{box-sizing:border-box;margin:0;padding:0}
html,body{width:1143px;height:1200px;overflow:hidden;background:var(--bg)}
.canvas{position:relative;width:1143px;height:1200px}
.flyer{position:absolute;top:60px;width:510px;height:1080px;background:var(--paper);overflow:hidden;font-family:"Poppins",sans-serif;color:var(--text)}
.flyer--front{left:41px}
.flyer--back{left:592px}
.flyer svg.shapes{position:absolute;inset:0}

/* header */
.brand{position:absolute;top:0;height:143px;border-bottom:1px solid var(--rule);margin:0 18px;width:474px}
.brand__mark{position:absolute;left:26px;top:44px;width:48px;height:48px;border-radius:50%;background:var(--tan)}
.brand__name{position:absolute;left:110px;top:34px;font-family:"Fredoka",sans-serif;font-weight:700;font-size:44px;color:var(--ink);line-height:1}
.brand__owner{position:absolute;left:188px;top:99px;font-family:"Playfair Display",serif;font-weight:700;font-size:14px;letter-spacing:3.4px;color:var(--ink)}

/* front */
.headline{position:absolute;left:0;top:165px;width:510px;text-align:center;font-family:"Fredoka",sans-serif;font-weight:700;font-size:27px;line-height:32px;color:var(--ink);text-transform:uppercase}
.photo{position:absolute;border-radius:50%;border:6px solid var(--white)}
.photo--portrait{left:26px;top:281px;width:338px;height:338px;background:radial-gradient(circle at 55% 40%,#e8d3c0 0%,#b9b7b3 45%,#6f7172 100%)}
.photo--pets{left:256px;top:482px;width:234px;height:234px;background:linear-gradient(180deg,#7f8f55 0%,#c98a45 50%,#a58b6c 100%)}
.owner-name{position:absolute;left:34px;top:628px;width:220px;text-align:center;font-family:"Fredoka",sans-serif;font-weight:700;font-size:33px;line-height:35px;color:var(--white)}
.intro{position:absolute;left:48px;top:790px;width:414px;text-align:center;font-size:11.5px;line-height:15.5px}
.slogan{position:absolute;left:0;top:882px;width:510px;text-align:center;font-family:"Kaushan Script",cursive;font-size:33px;color:var(--tan)}

/* contact */
.contact{position:absolute;display:grid;grid-template-columns:auto auto;column-gap:20px;row-gap:9px;font-style:normal;font-weight:600;font-size:12.5px;color:var(--white)}
.flyer--front .contact{left:48px;top:1011px}
.flyer--back .contact{left:44px;top:1006px;row-gap:8px}
.contact span{display:flex;align-items:center;gap:6px;white-space:nowrap}
.contact svg{width:13px;height:13px;flex:none}

/* back */
.service{position:absolute;left:41px;top:159px;width:420px;height:300px;border:3px solid var(--tan);border-radius:26px}
.service__title{position:absolute;left:68px;top:182px;width:366px;height:39px;border-radius:20px;background:var(--tan);color:var(--white);font-family:"Fredoka",sans-serif;font-weight:700;font-size:24px;line-height:39px;text-align:center}
.service__list{position:absolute;left:64px;top:236px;list-style:none;font-size:15.5px;line-height:26.5px;color:#333}
.service__list li{display:flex;align-items:center;gap:10px}
.service__list svg{width:14px;height:14px;flex:none}
.photo--meat{left:336px;top:306px;width:220px;height:220px;border:none;background:radial-gradient(circle at 40% 45%,#b4505c 0%,#8a2f3a 55%,#5a1d24 100%)}
.tcm__title{position:absolute;left:43px;top:484px;font-family:"Fredoka",sans-serif;font-weight:700;font-size:24px;color:var(--tan);text-transform:uppercase}
.tcm__text{position:absolute;left:43px;top:537px;width:440px;font-size:11.3px;line-height:15.2px;color:#222}
.tcm__text p+p{margin-top:15px}
.food-band{position:absolute;left:0;top:728px;width:510px;height:250px}
.photo--acupuncture{left:2px;top:704px;width:230px;height:230px;background:radial-gradient(circle at 50% 45%,#cfc7bd 0%,#a99d90 55%,#6e665e 100%)}
</style>
</head>
<body>
<div class="canvas">

  <section class="flyer flyer--front">
    <svg class="shapes" viewBox="0 0 510 1080" aria-hidden="true">
      <path d="M0,455 C20,560 120,640 260,640 C380,640 450,560 510,419 L510,745 C380,712 200,704 0,722 Z" fill="var(--tan)"/>
      <path d="M0,728 C180,708 380,716 510,752 L510,768 C380,742 180,752 0,762 Z" fill="var(--olive)"/>
      <path d="M0,1000 C150,930 350,945 510,940 L510,956 C350,962 150,955 0,1016 Z" fill="var(--tan)"/>
      <path d="M0,1008 C150,955 350,972 510,960 L510,1080 L0,1080 Z" fill="var(--olive)"/>
    </svg>

    <header class="brand">
      <span class="brand__mark"></span>
      <span class="brand__name">Pfotenruhe</span>
      <span class="brand__owner">MARLENE KÜHNEL</span>
    </header>

    <h1 class="headline">Tierernährungsberatung •<br>TCVM • Akupunktur in<br>Karlsruhe und Umgebung</h1>

    <div class="photo photo--portrait" role="img" aria-label="Foto: Therapeutin mit weißer Katze im Arm"></div>
    <div class="photo photo--pets" role="img" aria-label="Foto: Katze und Hund liegen zusammen im Freien"></div>

    <h2 class="owner-name">MARLENE<br>KÜHNEL</h2>

    <p class="intro">Mein Name ist Marlene Kühnel. Ich bin Tierernährungsberaterin für Hunde und Katzen, Akupunkteurin (TCVM) für Hunde, Katzen und Pferde und Katzenverhaltenstrainerin und somit in der optimalen Lage, die Erkrankung deines Tieres umfassend zu betrachten und zu behandeln.</p>

    <p class="slogan">Dein Tier in guten Händen!</p>

    <address class="contact">
      <span><svg viewBox="0 0 16 16"><circle cx="8" cy="8" r="8" fill="#fff"/><path d="M5,4 l2,0 l.6,2 -1,1 a5,5 0 0 0 2.4,2.4 l1,-1 2,.6 0,2 a1,1 0 0 1 -1,1 A7,7 0 0 1 4,5 a1,1 0 0 1 1,-1z" fill="var(--olive)"/></svg>0151 - 4830 2719</span>
      <span><svg viewBox="0 0 16 16"><circle cx="8" cy="8" r="8" fill="#fff"/><rect x="4" y="5" width="8" height="6" fill="none" stroke="var(--olive)" stroke-width="1.2"/><path d="M4,5 8,8.5 12,5" fill="none" stroke="var(--olive)" stroke-width="1.2"/></svg>info@pfotenruhe.de</span>
      <span><svg viewBox="0 0 16 16"><circle cx="8" cy="8" r="8" fill="#fff"/><circle cx="8" cy="8" r="4.5" fill="none" stroke="var(--olive)" stroke-width="1.1"/><path d="M3.5,8h9M8,3.5c-2,2.5-2,6.5,0,9M8,3.5c2,2.5,2,6.5,0,9" fill="none" stroke="var(--olive)" stroke-width="1"/></svg>pfotenruhe.de</span>
      <span><svg viewBox="0 0 16 16"><path d="M8,1a5,5 0 0 1 5,5c0,4-5,9-5,9S3,10,3,6a5,5 0 0 1 5-5z" fill="#fff"/><circle cx="8" cy="6" r="2" fill="var(--olive)"/></svg>Lindenweg 9a · 76139 Karlsruhe</span>
    </address>
  </section>

  <section class="flyer flyer--back">
    <svg class="shapes" viewBox="0 0 510 1080" aria-hidden="true">
      <path d="M0,995 C150,940 350,945 510,940 L510,955 C350,962 150,958 0,1010 Z" fill="var(--tan)"/>
      <path d="M0,1004 C150,958 350,972 510,958 L510,1080 L0,1080 Z" fill="var(--olive)"/>
    </svg>

    <header class="brand">
      <span class="brand__mark"></span>
      <span class="brand__name">Pfotenruhe</span>
      <span class="brand__owner">MARLENE KÜHNEL</span>
    </header>

    <div class="service"></div>
    <div class="photo photo--meat" role="img" aria-label="Foto: rohes Fleisch für Hundefutter"></div>
    <h2 class="service__title">UNSER SERVICE</h2>
    <ul class="service__list">
      <li><svg viewBox="0 0 14 14"><circle cx="7" cy="7" r="7" fill="var(--tan)"/><path d="M4,7.2 6.2,9.3 10,5" fill="none" stroke="#fff" stroke-width="1.6"/></svg>Katzenverhaltenstraining</li>
      <li><svg viewBox="0 0 14 14"><circle cx="7" cy="7" r="7" fill="var(--tan)"/><path d="M4,7.2 6.2,9.3 10,5" fill="none" stroke="#fff" stroke-width="1.6"/></svg>Ernährungsberatung für Hunde und Katzen</li>
      <li><svg viewBox="0 0 14 14"><circle cx="7" cy="7" r="7" fill="var(--tan)"/><path d="M4,7.2 6.2,9.3 10,5" fill="none" stroke="#fff" stroke-width="1.6"/></svg>Ganzheitliche Behandlung nach TCVM</li>
      <li><svg viewBox="0 0 14 14"><circle cx="7" cy="7" r="7" fill="var(--tan)"/><path d="M4,7.2 6.2,9.3 10,5" fill="none" stroke="#fff" stroke-width="1.6"/></svg>Akupunktur</li>
      <li><svg viewBox="0 0 14 14"><circle cx="7" cy="7" r="7" fill="var(--tan)"/><path d="M4,7.2 6.2,9.3 10,5" fill="none" stroke="#fff" stroke-width="1.6"/></svg>Laserbehandlung</li>
      <li><svg viewBox="0 0 14 14"><circle cx="7" cy="7" r="7" fill="var(--tan)"/><path d="M4,7.2 6.2,9.3 10,5" fill="none" stroke="#fff" stroke-width="1.6"/></svg>Chinesische Kräuterheilkunde</li>
      <li><svg viewBox="0 0 14 14"><circle cx="7" cy="7" r="7" fill="var(--tan)"/><path d="M4,7.2 6.2,9.3 10,5" fill="none" stroke="#fff" stroke-width="1.6"/></svg>Mykotherapie</li>
      <li><svg viewBox="0 0 14 14"><circle cx="7" cy="7" r="7" fill="var(--tan)"/><path d="M4,7.2 6.2,9.3 10,5" fill="none" stroke="#fff" stroke-width="1.6"/></svg>Darmaufbau</li>
    </ul>

    <h2 class="tcm__title">Was ist TCM?</h2>
    <div class="tcm__text">
      <p>Die traditionelle chinesische Medizin für Tiere (TCVM) ist ein ganzheitliches medizinisches System, das auf einer jahrtausendealten chinesischen Tradition basiert. Sie umfasst verschiedene Behandlungsmethoden wie Akupunktur, Moxibustion, Lasertherapie, Kräuterheilkunde, Ernährungstherapie und Tuina.</p>
      <p>Ziel der TCVM ist es, die Energie (Qi) wieder ins Gleichgewicht zu bringen und die Selbstheilungskräfte des Körpers zu aktivieren. Die chinesische Diagnostik ist sehr detaillierte und aufwändig, um krankmachende Disharmonien zu finden und diese zu entstören.</p>
    </div>

    <svg class="food-band" viewBox="0 0 510 250" role="img" aria-label="Foto: Schale mit frischem Tierfutter, Gemüse, Eiern, Fleisch und Hundekeksen auf dunklem Grund">
      <defs>
        <linearGradient id="foodTone" x1="0" y1="0" x2="1" y2="1">
          <stop offset="0" stop-color="#2a2623"/>
          <stop offset="0.5" stop-color="#6b3a2a"/>
          <stop offset="1" stop-color="#3a2a24"/>
        </linearGradient>
      </defs>
      <path d="M0,22 C120,30 230,8 330,4 C420,0 480,6 510,18 L510,222 C380,205 200,208 0,240 Z" fill="url(#foodTone)"/>
    </svg>
    <div class="photo photo--acupuncture" role="img" aria-label="Foto: Akupunkturnadeln im Bein eines Hundes"></div>

    <address class="contact">
      <span><svg viewBox="0 0 16 16"><circle cx="8" cy="8" r="8" fill="#fff"/><path d="M5,4 l2,0 l.6,2 -1,1 a5,5 0 0 0 2.4,2.4 l1,-1 2,.6 0,2 a1,1 0 0 1 -1,1 A7,7 0 0 1 4,5 a1,1 0 0 1 1,-1z" fill="var(--olive)"/></svg>0151 - 4830 2719</span>
      <span><svg viewBox="0 0 16 16"><circle cx="8" cy="8" r="8" fill="#fff"/><rect x="4" y="5" width="8" height="6" fill="none" stroke="var(--olive)" stroke-width="1.2"/><path d="M4,5 8,8.5 12,5" fill="none" stroke="var(--olive)" stroke-width="1.2"/></svg>info@pfotenruhe.de</span>
      <span><svg viewBox="0 0 16 16"><circle cx="8" cy="8" r="8" fill="#fff"/><circle cx="8" cy="8" r="4.5" fill="none" stroke="var(--olive)" stroke-width="1.1"/><path d="M3.5,8h9M8,3.5c-2,2.5-2,6.5,0,9M8,3.5c2,2.5,2,6.5,0,9" fill="none" stroke="var(--olive)" stroke-width="1"/></svg>pfotenruhe.de</span>
      <span><svg viewBox="0 0 16 16"><path d="M8,1a5,5 0 0 1 5,5c0,4-5,9-5,9S3,10,3,6a5,5 0 0 1 5-5z" fill="#fff"/><circle cx="8" cy="6" r="2" fill="var(--olive)"/></svg>Lindenweg 9a · 76139 Karlsruhe</span>
    </address>
  </section>

</div>
</body>
</html>
```